Belcotti Business Cards

Business cards for real estate
Target Market(s)
Real estate
Industry/Entity Type
Real Estate Agent
Font styles to use
Serif
Requirements
Must have
- Photo and logo

```html
<!DOCTYPE html>
<html lang="en">
<head>
<meta charset="UTF-8">
<title>Belcotti Realty – Business Card</title>
<link href="https://fonts.googleapis.com/css2?family=Cormorant+Garamond:wght@500&family=Lato:wght@400;700&display=swap" rel="stylesheet">
<style>
  :root {
    --backdrop: #e7e4e1;
    --card-white: #ffffff;
    --card-mist: #efecec;
    --band-black: #0d0d0d;
    --maroon: #7a1c22;
    --gold: #c9a45a;
    --ink: #1a1a1a;
    --light-text: #f2f2f2;
  }
  * { box-sizing: border-box; margin: 0; padding: 0; }
  html, body {
    width: 1200px; height: 900px; overflow: hidden;
    background: var(--backdrop);
  }
  .business-card {
    position: absolute;
    left: 80px; top: 128px;
    width: 1040px; height: 645px;
    background: linear-gradient(180deg, var(--card-white) 0%, var(--card-mist) 100%);
    overflow: hidden;
    box-shadow: 0 14px 40px rgba(0,0,0,0.18);
  }
  .accent-rule {
    position: absolute;
    left: 416px; right: 0; top: 320px; height: 9px;
    background: var(--maroon);
  }
  .contact-band {
    position: absolute;
    left: 416px; right: 0; top: 329px; bottom: 0;
    background: var(--band-black);
  }
  .agent-photo {
    position: absolute;
    left: 0; top: 0; width: 555px; height: 100%;
    background: linear-gradient(180deg, #ebe9e8 0%, #d8d2cd 30%, #6b6464 52%, #26262c 70%, #18181d 100%);
  }
  .brand {
    position: absolute;
    left: 470px; top: 96px;
    display: flex; align-items: center; gap: 34px;
  }
  .brand-square {
    width: 130px; height: 130px;
    background: var(--maroon);
  }
  .brand-name {
    font-family: "Cormorant Garamond", Georgia, serif;
    font-weight: 500;
    color: var(--ink);
    font-size: 56px;
    line-height: 1.0;
    letter-spacing: 2px;
    text-transform: uppercase;
  }
  .brand-name span { display: block; letter-spacing: 7px; }
  .contact-details {
    position: absolute;
    right: 72px; top: 340px;
    text-align: right;
    font-family: "Lato", Arial, sans-serif;
    color: var(--light-text);
    font-size: 27px;
    line-height: 1.45;
  }
  .agent-name {
    font-weight: 700; color: var(--gold);
    font-size: 36px; letter-spacing: 1px; line-height: 1.2;
  }
  .agent-title { margin-bottom: 10px; }
  .contact-line { display: flex; justify-content: flex-end; align-items: center; gap: 8px; }
  .contact-line svg { width: 22px; height: 22px; flex: none; }
  .office-address { margin-top: 12px; }
</style>
</head>
<body>
  <div class="business-card">
    <div class="accent-rule"></div>
    <div class="contact-band"></div>
    <div class="agent-photo" role="img" aria-label="Portrait photo of the managing director in a dark pinstripe suit and blue tie"></div>

    <div class="brand">
      <div class="brand-square"></div>
      <div class="brand-name">Belcotti<span>Realty</span></div>
    </div>

    <div class="contact-details">
      <div class="agent-name">MARCUS DELANEY</div>
      <div class="agent-title">Managing Director</div>
      <div class="contact-line">044-987 654 321
        <svg viewBox="0 0 24 24" fill="var(--gold)"><path d="M3 9c0-3 4-5 9-5s9 2 9 5l-4 1-1-3H8L7 10 3 9z"/><rect x="5" y="12" width="14" height="8" rx="1"/></svg>
      </div>
      <div class="contact-line">info@belcottihomes.com
        <svg viewBox="0 0 24 24"><rect x="3" y="6" width="18" height="12" fill="var(--gold)"/><path d="M3 6l9 7 9-7" stroke="var(--band-black)" stroke-width="1.5" fill="none"/></svg>
      </div>
      <div class="contact-line">www.belcottirealty.com
        <svg viewBox="0 0 24 24"><circle cx="12" cy="12" r="9" fill="var(--gold)"/><path d="M7 9c2 0 3 1 3 3s2 2 2 4M14 5c0 2 2 3 4 3" stroke="var(--band-black)" stroke-width="1.6" fill="none"/></svg>
      </div>
      <div class="office-address">218, Harbor Lane 45452, Country Name</div>
    </div>
  </div>
</body>
</html>
```